Corvantic Needs a Poster to Advertise a New Membership Offer

We need a Poster design for Corvantic Fitness Guild.
A first of it's kind membership, The Corvantic Fitness Guild combines the skills of our industry-leading Physiotherapists, Strength Coaches and Massage Therapists into one membership with a tailored plan to guide you through the fundamentals of Movement, Mobility and Recovery.
The concept is loosely based on the professional sports model, where every member of our team works together to produce lasting results for you. The final design should illustrate the bespoke nature of our program in a fun, supportive and professional space.
"Whether your aim is to be the best in the world, or the best in your world – it’s all the same to us."
Brand Guidelines
The poster should be on a black background and use our brand colour, lime green (hexcode #cefa08) as a highlight. Please don't overuse the highlight colour though. Generally, we opt for less bright colours and more of a 'street' look
Target Market(s)
The poster should attract predominantly female members, but should not exclude males. The target age range is 30-40 years female.
Industry/Entity Type
Health And Wellness
Requirements
Must have
- Must Include
• CFG logo
• Tag line " Shaping Steady, Nimble, Unbreakable People"
• Call to action "Join us"
• Sized to 600(W)x900(H)mm
• Text: "A first of it's kind membership, The Corvantic Fitness Guild combines the skills of our industry-leading Physiotherapists, Strength Coaches and Massage Therapists into one membership with a tailored plan to guide you through the fundamentals of Movement, Mobility and Recovery."
Nice to have
- Ideal Inclusions
• Corvantic logo
• Text "Membership Now Open"
• Web address: corvantic.com.au
Should not have
- Don't Use:
• Too much of the highlight colour
• Cartoon imagery
• Images that are too staged or revealing (clothing). Image should fit our target market of everyday active people, not elite athletes or models.

```html
<!DOCTYPE html>
<html lang="en">
<head>
<meta charset="utf-8">
<title>Corvantic Fitness Guild – Membership Poster</title>
<link rel="stylesheet" href="https://fonts.googleapis.com/css2?family=Saira+Condensed:wght@700;800&family=Fira+Sans:ital,wght@0,300;0,600;1,300&display=swap">
<style>
  :root {
    --ink: #0a080f;
    --lime: #cefa08;
    --white: #ffffff;
    --muted: #cfcfd2;
    --backdrop: #c4c4c4;
    --photo-light: #6d6d6f;
    --photo-mid: #2c2b30;
  }
  * { margin: 0; padding: 0; box-sizing: border-box; }
  html, body {
    width: 859px; height: 1200px; overflow: hidden;
    background: var(--backdrop);
  }
  .poster {
    position: absolute; left: 29.5px; top: 0;
    width: 800px; height: 1200px;
    background: var(--ink);
    overflow: hidden;
    color: var(--white);
  }
  .poster__photo {
    position: absolute; left: 360px; top: 140px;
    width: 440px; height: 880px;
    background:
      radial-gradient(ellipse 45% 30% at 60% 38%, var(--photo-light), transparent 70%),
      radial-gradient(ellipse 55% 50% at 55% 62%, var(--photo-mid), transparent 75%);
  }
  .poster__smoke {
    position: absolute; left: 0; top: 520px;
    width: 520px; height: 480px;
    background: radial-gradient(ellipse 60% 45% at 30% 35%, #25242a, transparent 75%);
  }
  .poster__bands { position: absolute; inset: 0; }
  .brand-mark {
    position: absolute; left: 66px; top: 88px;
    font-family: "Fira Sans", sans-serif; font-weight: 600;
    font-size: 84px; line-height: 1; letter-spacing: -1px;
    color: var(--white);
  }
  .headline {
    position: absolute; left: 60px; top: 246px;
    font-family: "Saira Condensed", sans-serif; font-weight: 700;
    font-size: 61px; line-height: 57px; text-transform: uppercase;
    letter-spacing: 0.5px;
  }
  .intro {
    position: absolute; left: 60px; top: 604px;
    font-family: "Fira Sans", sans-serif; font-weight: 300;
    font-size: 23.5px; line-height: 33px;
    white-space: nowrap;
  }
  .intro em { font-style: italic; }
  .intro strong { font-weight: 600; }
  .cta {
    position: absolute; left: 58px; top: 1108px;
    width: 334px; height: 39px;
    font-family: "Saira Condensed", sans-serif; font-weight: 800;
    font-size: 32px; text-transform: uppercase;
  }
  .cta svg { position: absolute; inset: 0; }
  .cta__label, .cta__status {
    position: absolute; top: 0; line-height: 39px;
  }
  .cta__label { left: 11px; color: var(--white); }
  .cta__status { left: 202px; color: var(--ink); }
  .wordmark {
    position: absolute; right: 57px; top: 1098px;
    font-family: "Fira Sans", sans-serif; font-weight: 600;
    font-size: 52px; line-height: 1; color: var(--white);
  }
  .join {
    position: absolute; right: 57px; top: 1160px;
    font-family: "Fira Sans", sans-serif; font-weight: 300;
    font-size: 15px; line-height: 1; color: var(--muted);
    letter-spacing: 0.3px;
  }
  .join strong { font-weight: 600; color: var(--white); }
</style>
</head>
<body>
  <main class="poster">
    <div class="poster__smoke" role="img" aria-label="Dark smoky haze in the background"></div>
    <div class="poster__photo" role="img" aria-label="Black and white photograph of a female athlete sprinting toward the viewer, wearing dark sportswear with lime armbands"></div>

    <svg class="poster__bands" width="800" height="1200" viewBox="0 0 800 1200" aria-hidden="true">
      <polygon fill="var(--lime)" points="0,487 174,551 800,363 800,380 174,569 0,505"/>
      <polygon fill="var(--lime)" points="0,1056 800,925 800,940 0,1072"/>
    </svg>

    <div class="brand-mark">CFG</div>

    <h1 class="headline">Shaping<br>Steady, Nimble,<br>Unbreakable<br>People</h1>

    <p class="intro">
      A first of it’s kind membership,<br>
      The <em>Corvantic Fitness Guild</em><br>
      combines the skills of our<br>
      industry-leading<br>
      <strong>Physiotherapists, Strength<br>
      Coaches and Massage Therapists</strong><br>
      into one membership with a<br>
      tailored plan to guide you through<br>
      the fundamentals of Movement,<br>
      Mobility and Recovery."
    </p>

    <div class="cta">
      <svg width="334" height="39" viewBox="0 0 334 39" aria-hidden="true">
        <rect x="0.75" y="0.75" width="332.5" height="37.5" fill="none" stroke="var(--lime)" stroke-width="1.5"/>
        <polygon fill="var(--lime)" points="180,0 334,0 334,39 180,39 191,19.5"/>
      </svg>
      <span class="cta__label">Membership</span>
      <span class="cta__status">Now Open</span>
    </div>

    <div class="wordmark">corvantic</div>
    <p class="join"><strong>Join us</strong> at corvantic.com.au</p>
  </main>
</body>
</html>
```